Business card design for global fintech startup

Veltrix is a modern payments platform for the global insurance industry, serving international health, life, and travel insurers, MGAs, brokers, and partners.

We need a professional, premium business card for use at insurance conferences and executive meetings. The goal is to create a card that feels trustworthy, modern, and high-quality, while still being distinctive and memorable in a stack of business cards.

Target audience:
Senior insurance executives (VP, C-suite).

Design goals:
Clear, professional, and credible
Modern but not trendy
Premium and well-structured
Easy to read and practical for networking

Brand direction:
Brand-first (company over individual)
Follow existing brand guidelines where possible
Clean layout, strong hierarchy, excellent readability

Must include:
Name
Title
Company name (Veltrix)
Logo
Email
Phone/Whatsapp
Website (www.withveltrix.example)
Tagline - Certainty that moves capital

Materials & finish:
Open to designer recommendations for premium look and feel.

Please avoid:
Flashy or trendy startup styles
Generic insurance icons or clichés
Cluttered layouts or hard-to-read text

Deliverables:
Front and back business card, print-ready files.

Target Market(s)

Global Insurance executives

Industry/Entity Type

Fintech, Insurtech, Insurance, Financial Services

Contact Information for Business Card

Name Title Company name (Veltrix) Logo Email Phone/Whatsapp Website (www.withveltrix.example) Tagline - Certainty that moves capital

Font styles to use
Other font styles liked:
• See brand guidelines

Requirements
Nice to have
• something that stands out/makes us more memorable while still remaining professional
Should not have
• Please avoid: Flashy or trendy startup styles Generic insurance icons or clichés Cluttered layouts or hard-to-read text

```html
<!DOCTYPE html>
<html lang="en">
<head>
<meta charset="utf-8">
<title>Veltrix Business Cards</title>
<link href="https://fonts.googleapis.com/css2?family=Ubuntu:wght@400;500;700&display=swap" rel="stylesheet">
<style>
  :root {
    --bg: #dcdcdc;
    --card: #ffffff;
    --ink: #111111;
    --ink-soft: #222222;
    --band: #2e2d30;
    --band-text: #ffffff;
    --accent: #f08a1c;
    --peach: #f9d3b2;
    --lavender: #d9cce6;
    --sky: #cfe6f5;
    --cream: #fdf0cc;
  }
  * { margin: 0; padding: 0; box-sizing: border-box; }
  html, body {
    width: 1200px; height: 900px; overflow: hidden;
    background: var(--bg);
    font-family: "Ubuntu", sans-serif;
    color: var(--ink);
  }
  .sheet { position: relative; width: 1200px; height: 900px; }
  .card {
    position: absolute; width: 514px; height: 308px;
    background: var(--card);
    box-shadow: 0 6px 16px rgba(0,0,0,0.18);
    overflow: hidden;
  }
  .card--front-top { left: 72px; top: 127px; }
  .card--front-bottom { left: 72px; top: 464px; }
  .card--back-band { left: 616px; top: 127px; }
  .card--back-wash { left: 616px; top: 464px; }

  .wordmark {
    display: flex; align-items: center;
    font-weight: 500; letter-spacing: 0.08em; color: var(--ink);
    text-transform: uppercase;
  }
  .wordmark__dot { border-radius: 50%; background: var(--accent); flex: none; }
  .wordmark--large {
    position: absolute; left: 0; right: 0; top: 0; bottom: 0;
    justify-content: center; font-size: 50px; gap: 20px;
  }
  .wordmark--large .wordmark__dot { width: 40px; height: 40px; }
  .wordmark--small {
    position: absolute; left: 57px; top: 73px; font-size: 25px; gap: 12px;
  }
  .wordmark--small .wordmark__dot { width: 22px; height: 22px; }

  .contact { position: absolute; left: 62px; top: 197px; font-size: 11.5px; line-height: 14px; color: var(--ink-soft); }
  .contact__name { font-size: 15.5px; font-weight: 700; color: var(--ink); line-height: 18px; }
  .contact__title { margin-bottom: 16px; }

  .tagline-band {
    position: absolute; right: 0; top: 0; width: 46px; height: 100%;
    background: var(--band);
    display: flex; align-items: center; justify-content: center;
  }
  .tagline-band__text {
    writing-mode: vertical-rl; transform: rotate(180deg);
    color: var(--band-text); font-size: 13px; letter-spacing: 0.14em;
    text-transform: uppercase; white-space: nowrap;
  }

  .brand-wash {
    position: absolute; right: 0; top: 0; width: 270px; height: 100%;
    background: linear-gradient(160deg, var(--peach) 0%, var(--lavender) 45%, var(--sky) 75%, var(--cream) 100%);
    opacity: 0.85;
  }
  .tagline-stack {
    position: absolute; right: 14px; top: 54px; width: 100px;
    text-align: center; color: var(--band-text);
    font-size: 14.5px; line-height: 18px; text-transform: uppercase;
  }
</style>
</head>
<body>
<main class="sheet">
  <section class="card card--front-top">
    <div class="wordmark wordmark--large"><span class="wordmark__dot"></span>Veltrix</div>
  </section>

  <section class="card card--front-bottom">
    <div class="wordmark wordmark--large"><span class="wordmark__dot"></span>Veltrix</div>
  </section>

  <section class="card card--back-band">
    <div class="wordmark wordmark--small"><span class="wordmark__dot"></span>Veltrix</div>
    <div class="contact">
      <p class="contact__name">Daniel Marsh</p>
      <p class="contact__title">Managing Director</p>
      <p>P&nbsp; 555 0190 2244</p>
      <p>E&nbsp; d.marsh@withveltrix.example</p>
      <p>W www.withveltrix.example</p>
    </div>
    <div class="tagline-band"><span class="tagline-band__text">Certainty that moves capital</span></div>
  </section>

  <section class="card card--back-wash">
    <div class="brand-wash" role="img" aria-label="Soft brand colour wash in peach, lavender and sky blue"></div>
    <p class="tagline-stack">Certainty<br>that<br>moves<br>capital</p>
    <div class="wordmark wordmark--small"><span class="wordmark__dot"></span>Veltrix</div>
    <div class="contact">
      <p class="contact__name">Daniel Marsh</p>
      <p class="contact__title">Managing Director</p>
      <p>P&nbsp; 555 0190 2244</p>
      <p>E&nbsp; d.marsh@withveltrix.example</p>
      <p>W www.withveltrix.example</p>
    </div>
  </section>
</main>
</body>
</html>
```